Law Firm Website, easily updated by User

We are a regional Labor and Employment Law Firm with a tired outdated website. We are looking for a clean easy to use website that will allow us to easily update information and articles in house. Our current website can be found at www.quillbrookcounsel.com

Industry/Entity Type

Labor

Number of Pages Required

5+ page

Colors
0655a3

Requirements
Must have
• Content easily updated by user
Nice to have
• crisp clean pages
Should not have
• stock pictures

```html
<!DOCTYPE html>
<html lang="en">
<head>
<meta charset="utf-8">
<title>Quillbrook &amp; Associates, P.C.</title>
<link rel="stylesheet" href="https://fonts.googleapis.com/css2?family=Pathway+Gothic+One&family=Noto+Serif&family=Open+Sans:wght@700&family=Arimo:wght@400&display=swap">
<style>
:root{
  --brand:#2e3b8c;
  --ink:#1d1d1f;
  --accent:#c0272d;
  --footer:#23262b;
  --white:#ffffff;
  --hero-dark:#4a1f0e;
  --hero-mid:#9a5a26;
  --hero-light:#d9b27a;
}
*{margin:0;padding:0;box-sizing:border-box}
html,body{width:1200px;height:1099px;overflow:hidden;background:var(--white)}
body{position:relative;font-family:"Arimo",Arial,sans-serif;color:var(--ink)}
.brand{position:absolute;left:164px;top:44px;display:flex;align-items:center;gap:10px}
.brand-square{width:34px;height:34px;background:var(--brand)}
.brand-name{font-family:"Noto Serif",serif;font-size:24px;color:var(--ink);line-height:1}
.brand-tag{position:absolute;left:208px;top:88px;font-family:"Noto Serif",serif;font-size:9px;color:var(--ink);border-top:2px solid var(--brand);padding-top:2px;width:280px}
.social{position:absolute;left:675px;top:11px;display:flex;gap:4px}
.social span{width:31px;height:31px;background:var(--brand);display:block}
.contact{position:absolute;left:801px;top:18px;font-family:"Pathway Gothic One",sans-serif;font-size:16px;color:var(--accent)}
.nav{position:absolute;right:205px;top:83px;display:flex;gap:15px;font-family:"Pathway Gothic One",sans-serif;font-size:18px;color:var(--ink);text-transform:uppercase}
.hero{position:absolute;left:0;top:145px;width:1200px;height:338px;background:linear-gradient(100deg,var(--hero-dark) 0%,var(--hero-mid) 45%,var(--hero-light) 100%)}
.hero-kicker{position:absolute;left:198px;top:156px;font-family:"Open Sans",sans-serif;font-weight:700;font-size:19px;letter-spacing:-.5px;color:var(--white)}
.hero-line{position:absolute;left:198px;top:195px;font-family:"Noto Serif",serif;font-size:27px;color:var(--white)}
.hero-title{position:absolute;left:198px;top:231px;font-family:"Noto Serif",serif;font-size:38px;color:var(--white);text-shadow:0 2px 3px rgba(0,0,0,.4)}
.portrait{position:absolute;top:137px;width:110px;height:162px;border:2px solid var(--white);background:linear-gradient(#8a8a8a,#2a2a30)}
.about-title{position:absolute;left:185px;top:512px;font-family:"Pathway Gothic One",sans-serif;font-size:28px;color:var(--brand)}
.about-text{position:absolute;left:185px;top:564px;width:557px;font-size:12px;line-height:17px;text-align:justify}
.about-text p+p{margin-top:17px}
.about-mark{position:absolute;left:790px;top:585px;display:flex;align-items:center;gap:8px;font-family:"Noto Serif",serif;font-size:22px;color:var(--brand)}
.about-mark span.sq{width:26px;height:26px;background:var(--brand)}
.feature{position:absolute;top:765px;width:262px}
.feature-icon{width:140px;height:112px;background:#2a2a2c;border-radius:4px}
.feature h2{font-family:"Pathway Gothic One",sans-serif;font-weight:400;font-size:27px;margin-top:20px;line-height:1}
.feature p{font-size:10.5px;line-height:17px;margin-top:8px;text-align:justify}
.footer{position:absolute;left:0;top:1055px;width:1200px;height:44px;background:var(--footer);border-top:2px solid #111;color:var(--white);font-size:10.5px;text-align:center;line-height:42px}
</style>
</head>
<body>
<header>
  <div class="brand"><span class="brand-square"></span><span class="brand-name">Quillbrook &amp; Associates, P.C.</span></div>
  <div class="brand-tag">EMPLOYMENT COUNSELING, LITIGATION, LABOR &amp; BENEFITS LAW</div>
  <div class="social" aria-label="Social links"><span></span><span></span><span></span></div>
  <div class="contact">555 010 4821 | info@quillbrookcounsel.com</div>
  <nav class="nav"><span>Home</span><span>About</span><span>Attorneys</span><span>Practice Areas</span><span>Contact Us</span></nav>
</header>
<section class="hero" role="img" aria-label="Wooden gavel resting on a signed agreement">
  <div class="hero-kicker">COUNSELING AND ADVISING CLIENT</div>
  <div class="hero-line">Exclusively on</div>
  <div class="hero-title">Laws of the Workplace</div>
  <div class="portrait" style="left:651px" role="img" aria-label="Attorney portrait"></div>
  <div class="portrait" style="left:786px" role="img" aria-label="Attorney portrait"></div>
  <div class="portrait" style="left:913px" role="img" aria-label="Attorney portrait"></div>
</section>
<section>
  <h1 class="about-title">About QUILLBROOK &amp; ASSOCIATES</h1>
  <div class="about-text">
    <p>QUILLBROOK &amp; ASSOCIATES, P.C. handles only labor, employment and benefits matters. This includes representing employers in state and federal court, before administrative and quasi-judicial agencies, and in negotiations, arbitrations and union organizing campaigns.</p>
    <p>Our attorneys provide a diverse range of counseling and training in areas of the law such as discrimination, sexual harassment, wage and hour issues, Family and Medical Leave Act, HIPPA and reductions-in-force. The attorneys provide hands-on assistance and guidance in the event of government audits, strikes and other daily crises.</p>
  </div>
  <div class="about-mark"><span class="sq"></span>Quillbrook</div>
</section>
<section>
  <div class="feature" style="left:174px">
    <div class="feature-icon" role="img" aria-label="Open law book icon"></div>
    <h2>Practice Areas</h2>
    <p>Lorem ipsum dolor sit amet, consectetur adipiscing elit. Sed at ante. Mauris eleifend, quam a vulputate dictum, massa quam dapibus leo, eget vulputate orci purus ut lorem. In fringilla mi in ligula. Pellentesque aliquam quam vel dolor. Nunc adipiscing. Sed quam odio,</p>
  </div>
  <div class="feature" style="left:466px">
    <div class="feature-icon" role="img" aria-label="Lawyer with document icon"></div>
    <h2>Legal Costs</h2>
    <p>Lorem ipsum dolor sit amet, consectetur adipiscing elit. Sed at ante. Mauris eleifend, quam a vulputate dictum, massa quam dapibus leo, eget vulputate orci purus ut lorem. In fringilla mi in ligula. Pellentesque aliquam quam vel dolor. Nunc adipiscing. Sed quam odio, tempus ac, aliquam molestie, varius ac, tellus.</p>
  </div>
  <div class="feature" style="left:787px">
    <div class="feature-icon" role="img" aria-label="Gavel icon"></div>
    <h2>Recent Cases</h2>
    <p>Lorem ipsum dolor sit amet, consectetur adipiscing elit. Sed at ante. Mauris eleifend, quam a vulputate dictum, massa quam dapibus leo, eget vulputate orci purus ut lorem. In fringilla mi in ligula. Pellentesque aliquam quam vel dolor. Nunc adipiscing. Sed quam odio, tempus ac, aliquam molestie, varius ac, tellus.</p>
  </div>
</section>
<footer class="footer">Copyright 2015 Quillbrook &amp; Associates, P.C. - Terms &amp; Conditions | Privacy Policy</footer>
</body>
</html>
```